Website redesign for fast growing company looking to present a unique image

We're looking to revamp our online image to represent the professional, accomplished company we have become. We want to move beyond a templated look and feel to a custom design - we are eager to have you design a new public face for us! In particular, we need creative ways to display text to stand out. We are reaching top-level, C-suite executives and want to give them the confidence that we have the skills, talent, expertise, and knowledge to help their companies grow.

Target Market(s)

contact centers, business process outsourcing

Industry/Entity Type

Call Center

Coding

Coded - Design and coding required

Number of Pages Required

4 page

Font styles to use
Sans Serif

Colors

Designer to choose colors to be used in the design.

Requirements
Must have
• Designed for a professional audience - C-suite executives - but that also shows our personality as a company that is nimble, personable, trustworthy, and smart. Must be lively, but not quirky. Professional, but not overly formal. Be bold with choices for imagery - we want to look unique so go beyond traditional "business/corporate" stock photos. Instead use imagery similar to what is on our staging website - korvanta.com/staging. Do not use the "neon" sign. Use colors to match and complement our logo - bright orange and dark blue. Creative text boxes that we can use throughout the site. I have attached pages of our current staging site to display some of the types of imagery that might work. We are looking for "professional with a personality" Note: this design will be transferred into a Wordpress framework.
Nice to have
• We like the animated text features of the Tellbrook.com site - bold colors, great display of text features that break up the page and engage people to continue scrolling.
Should not have
• Cheesy stock photos of call center agents wearing headsets. Overly used stock photos of professionals in suits shaking hands, high-rise buildings, connection/network graphics. Current management does not like the neon sign graphics displayed on our staging site (korvanta.com/staging). We do not like style of sites that use cartoon-like icons and figures.

```html
<!DOCTYPE html>
<html lang="en">
<head>
<meta charset="utf-8">
<title>Korvanta — Contact Center Solutions</title>
<link rel="stylesheet" href="https://fonts.googleapis.com/css2?family=Hind:wght@400;500;600;700&family=Raleway:wght@400;500;600;700&display=swap">
<style>
:root{
  --navy:#263a5f;
  --navy-dark:#1d2d4b;
  --orange:#f26f21;
  --blue:#0b4fa0;
  --ink:#222;
  --muted:#666;
  --light:#f5f5f5;
}
*{box-sizing:border-box;margin:0;padding:0}
html,body{width:1200px;height:3640px;overflow:hidden}
body{font-family:"Raleway",sans-serif;color:var(--ink);background:#fff;position:relative}
.abs{position:absolute}
h1,h2,h3{font-family:"Hind",sans-serif}

/* top bar */
.topbar{position:absolute;left:0;top:0;width:1200px;height:47px;background:var(--navy)}
.brand{position:absolute;left:93px;top:10px;display:flex;align-items:center;gap:8px;color:#fff;font-family:"Raleway",sans-serif;font-weight:600;font-size:22px;line-height:26px}
.brand-mark{width:14px;height:14px;background:#fff;border-radius:50%}
.contact-top{position:absolute;left:520px;top:6px;color:#fff;display:flex;gap:10px;align-items:center}
.contact-top .ico{width:26px;height:26px;background:#fff;border-radius:4px;display:flex;align-items:center;justify-content:center}
.contact-top .phone{font-size:16px;font-weight:600;line-height:16px}
.contact-top .mail{font-size:11px;opacity:.8}
.apply{position:absolute;left:994px;top:6px;width:112px;height:34px;background:var(--orange);color:#fff;font-size:11px;font-weight:600;display:flex;align-items:center;justify-content:center}

.nav{position:absolute;left:0;top:47px;width:1200px;height:45px;background:#fff}
.nav ul{list-style:none;display:flex;position:absolute;left:93px;top:15px;font-size:12px;font-weight:600}
.nav li{margin-right:49px}
.nav li.active{color:var(--orange)}
.nav .search{position:absolute;left:527px;top:14px;border-left:1px solid #ccc;padding-left:12px;height:18px}
.socials{display:flex;gap:5px}
.socials span{width:22px;height:22px;border-radius:50%;background:var(--orange);display:block}
.nav .socials{position:absolute;left:1006px;top:11px}

/* hero */
.hero{position:absolute;left:0;top:92px;width:1200px;height:508px;background:var(--navy)}
.hero .eyebrow{position:absolute;left:93px;top:135px;color:#fff;font-size:22px;font-family:"Hind",sans-serif;font-weight:400}
.hero h1{position:absolute;left:93px;top:160px;color:#fff;font-size:46px;line-height:48px;font-weight:700}
.hero p{position:absolute;left:93px;top:270px;width:470px;color:#fff;font-size:15px;line-height:25px}
.btn{display:flex;align-items:center;justify-content:center;color:#fff;font-size:11px;font-weight:700}
.hero .btn{position:absolute;left:94px;top:332px;width:107px;height:35px;background:var(--orange)}
.hero-art{position:absolute;left:0;top:0}

/* ready */
.ready-eyebrow{position:absolute;left:674px;top:765px;font-size:15px;color:#333}
.ready h2{position:absolute;left:674px;top:783px;font-size:38px;font-weight:700;letter-spacing:1px}
.ready p{position:absolute;left:674px;top:836px;width:436px;font-size:12.5px;line-height:22px;color:#555}
.ready .btn{position:absolute;left:675px;top:947px;width:103px;height:35px;background:var(--blue)}

/* pillars */
.pillars h2{position:absolute;left:0;width:1200px;top:1140px;text-align:center;font-size:40px;font-weight:700;letter-spacing:1px}
.pillars .sub{position:absolute;left:0;width:1200px;top:1200px;text-align:center;font-size:14px;color:#555}
.circle{position:absolute;border-radius:50%;display:flex;flex-direction:column;align-items:center;justify-content:center;text-align:center;font-weight:700;font-size:15px;color:var(--orange)}
.circle.ring-blue{border:1.5px solid var(--blue)}
.circle.ring-orange{border:1.5px solid var(--orange)}
.circle.focus{background:var(--blue);color:#fff;border:4px solid #2c66b3}
.circle.focus small{font-weight:400;font-size:9.5px;line-height:14px;margin-top:10px;width:172px}

/* benefits */
.benefits{position:absolute;left:0;top:1505px;width:1200px;height:396px;background:var(--light);overflow:hidden}
.benefits .eyebrow{position:absolute;left:92px;top:50px;font-size:16px;color:#333}
.benefits h2{position:absolute;left:92px;top:70px;font-size:38px;font-weight:700;letter-spacing:1px}
.benefits ul{position:absolute;left:93px;top:127px;list-style:none;font-size:13px;color:#333}
.benefits li{height:34px}
.benefits li::before{content:"";display:inline-block;width:4px;height:4px;background:var(--orange);margin-right:6px;vertical-align:middle}
.benefits b{color:#111}

/* outsourcing */
.outs h2{position:absolute;left:0;width:1200px;top:1948px;text-align:center;font-size:40px;font-weight:700;letter-spacing:1px}
.outs .sub{position:absolute;left:0;width:1200px;top:2002px;text-align:center;font-size:13.5px;color:#555}
.card{position:absolute;top:2134px;width:239px;height:276px;border-radius:10px}
.card.orange{background:var(--orange)}
.card.blue{background:var(--blue)}
.card .panel-wrap{position:absolute;left:15px;top:-78px;width:209px;height:268px;filter:drop-shadow(0 3px 6px rgba(0,0,0,.22))}
.card .panel{position:absolute;inset:0;background:#fff;border-radius:8px;clip-path:polygon(0 9%,100% 0,100% 100%,0 100%)}
.card .notch{position:absolute;left:147px;top:190px;width:0;height:0;border-left:14px solid transparent;border-right:14px solid transparent;border-top:18px solid #fff}
.card ul{position:absolute;left:10px;top:62px;width:185px;list-style:none;font-size:10.5px;line-height:15.5px;color:#777}
.card li{margin-bottom:16px;padding-left:9px;position:relative}
.card li::before{content:"";position:absolute;left:0;top:6px;width:3px;height:3px;background:var(--blue)}
.card .num{position:absolute;left:10px;top:226px;color:#fff;font-family:"Hind",sans-serif;font-weight:700;font-size:34px}
.card .title{position:absolute;left:70px;top:220px;color:#fff;font-family:"Hind",sans-serif;font-size:19px;line-height:22px;font-weight:500}

/* market */
.market{position:absolute;left:0;top:2499px;width:1200px;height:396px;background:var(--light)}
.market h2{position:absolute;left:0;width:1200px;top:50px;text-align:center;font-size:40px;font-weight:700;letter-spacing:1px}
.market .sub{position:absolute;left:0;width:1200px;top:103px;text-align:center;font-size:13.5px;color:#555}
.tile{position:absolute;top:141px;width:245px;text-align:center}
.tile .photo{width:245px;height:142px;border-radius:50% 50% 50% 50% / 55% 55% 45% 45%}
.tile .kind{font-size:14px;color:#333;margin-top:24px}
.tile .name{font-size:17px;font-weight:600;color:#111;margin-top:2px}
.arrow{position:absolute;top:196px;width:38px;height:30px;background:var(--blue);color:#fff;display:flex;align-items:center;justify-content:center;font-size:14px}
.arrow.left{left:0;border-radius:0 15px 15px 0}
.arrow.right{left:1162px;border-radius:15px 0 0 15px}

/* economics */
.econ{position:absolute;left:0;top:2895px;width:1200px;height:332px;background:linear-gradient(180deg,#0b4fa0,#0a4a98)}
.econ h2{position:absolute;left:0;width:1200px;top:48px;text-align:center;color:#fff;font-size:42px;font-weight:700;letter-spacing:1px}
.econ p{position:absolute;left:170px;width:860px;top:108px;text-align:center;color:#cfe0ff;font-size:14px;line-height:23px}
.econ .pill{position:absolute;left:249px;top:168px;width:701px;height:103px;border-radius:52px;background:#0f3f80}
.econ .field{position:absolute;top:200px;width:198px;height:39px;background:#fff;border-radius:20px;font-size:11px;padding:13px 18px;color:#222}
.econ .go{position:absolute;left:711px;top:200px;width:198px;height:39px;background:var(--orange);border-radius:20px;color:#fff;font-size:11px;font-weight:700;display:flex;align-items:center;justify-content:center}

/* footer */
.footer{position:absolute;left:0;top:3227px;width:1200px;height:413px;background:#f7f7f7}
.footer h3{font-family:"Hind",sans-serif;font-weight:400;font-size:20px;color:#222}
.fcol{position:absolute;top:54px}
.fcol ul{list-style:none;font-size:11px;color:#444;margin-top:4px}
.fcol li{height:31.5px}
.fcol .addr{font-size:11px;line-height:17px;color:#444;margin-top:6px;width:250px}
.fcol .line{font-size:11px;color:#444;margin-top:20px}
.ffield{position:absolute;left:807px;background:#fff;border:1px solid #ccc;font-size:10px;padding:8px 10px}
.send{position:absolute;left:1032px;top:257px;width:73px;height:31px;background:var(--blue);color:#fff;font-size:11px;font-weight:700;display:flex;align-items:center;justify-content:center}
.footer .socials{position:absolute;left:551px;top:306px}
.copy{position:absolute;left:0;width:1200px;top:342px;text-align:center;font-size:10.5px;color:#444}
.copy span{color:var(--orange)}
</style>
</head>
<body>

<header>
  <div class="topbar">
    <div class="brand"><span class="brand-mark"></span>Korvanta</div>
    <div class="contact-top">
      <div class="ico"><svg width="14" height="14" viewBox="0 0 24 24"><path d="M2 11 22 3 18 21 11 15 17 8 8 14Z" fill="#263a5f"/></svg></div>
      <div><div class="phone">+1 555.014.2290</div><div class="mail">info@korvanta.com</div></div>
    </div>
    <div class="apply">APPLY ONLINE</div>
  </div>
  <nav class="nav">
    <ul>
      <li class="active">HOME</li><li>MARKETS WE SERVE</li><li>ABOUT US</li><li>CONTACT</li>
    </ul>
    <div class="search"><svg width="14" height="14" viewBox="0 0 24 24"><circle cx="10" cy="10" r="7" fill="none" stroke="#333" stroke-width="2.5"/><path d="M15 15 21 21" stroke="#333" stroke-width="2.5"/></svg></div>
    <div class="socials"><span></span><span></span><span></span><span></span></div>
  </nav>
</header>

<section class="hero">
  <svg class="hero-art" width="1200" height="540" viewBox="0 0 1200 540">
    <defs>
      <clipPath id="heroClip"><rect x="0" y="0" width="1200" height="540"/></clipPath>
      <linearGradient id="heroPhoto" x1="0" y1="0" x2="1" y2="1">
        <stop offset="0" stop-color="#e9e4de"/><stop offset="1" stop-color="#b9aca0"/>
      </linearGradient>
    </defs>
    <g clip-path="url(#heroClip)">
      <rect x="20" y="0" width="26" height="210" rx="13" fill="var(--navy-dark)"/>
      <rect x="48" y="0" width="26" height="120" rx="13" fill="var(--navy-dark)"/>
      <path d="M690 40 775 0 800 0 700 58Z" fill="var(--orange)"/>
      <path d="M1030 495 1080 462 1092 478 1042 510Z" fill="var(--orange)"/>
      <circle cx="880" cy="300" r="310" fill="none" stroke="var(--navy-dark)" stroke-width="14"/>
      <circle role="img" aria-label="Photo of a young woman working at a laptop in a bright office" cx="905" cy="255" r="300" fill="url(#heroPhoto)"/>
    </g>
  </svg>
  <div class="eyebrow">GET MORE FROM</div>
  <h1>YOUR CUSTOMER<br>INTERACTIONS</h1>
  <p>Lift Your Top and Bottom Lines with Professional Outsourcing Solutions from Korvanta</p>
  <div class="btn">GET STARTED</div>
</section>

<section class="ready">
  <svg class="abs" style="left:92px;top:655px" width="510" height="445" viewBox="0 0 510 445">
    <path d="M150 20 Q220 -10 300 40 Q420 40 490 160 Q530 280 420 360 Z" fill="var(--orange)"/>
    <defs><linearGradient id="teamPhoto" x1="0" y1="0" x2="1" y2="1"><stop offset="0" stop-color="#d8d2c6"/><stop offset="1" stop-color="#8d7c6a"/></linearGradient></defs>
    <path role="img" aria-label="Photo of smiling colleagues collaborating around a table" d="M60 60 Q140 10 260 60 Q400 60 470 170 Q510 290 400 370 Q300 445 170 440 Q40 420 6 290 Q-10 140 60 60Z" fill="url(#teamPhoto)"/>
  </svg>
  <div class="ready-eyebrow">It's A New World.</div>
  <h2>ARE YOU READY?</h2>
  <p>It's time to find solutions that deliver more value. Shed the manual interactions that cost you money and distract you from your core. Get more by partnering with Korvanta for Customer Service, Tech Support, and Business Process Outsourcing solutions.</p>
  <div class="btn">READ MORE</div>
</section>

<section class="pillars">
  <h2>BETTER. FASTER. LEANER. SMARTER</h2>
  <div class="sub">GET MORE FROM YOUR CUSTOMER INTERACTIONS</div>
  <div class="circle ring-blue" style="left:116px;top:1265px;width:158px;height:158px">MORE VALUE</div>
  <div class="circle ring-orange" style="left:318px;top:1265px;width:158px;height:158px">MORE<br>PERFORMANCE</div>
  <div class="circle focus" style="left:499px;top:1244px;width:200px;height:200px">MORE FOCUS<small>If you use this site regularly and would like to help keep the site on the Internet</small></div>
  <div class="circle ring-orange" style="left:722px;top:1265px;width:158px;height:158px">MORE LOYALTY</div>
  <div class="circle ring-blue" style="left:926px;top:1265px;width:158px;height:158px">MORE INSIGHTS</div>
</section>

<section class="benefits">
  <svg class="abs" style="left:0;top:0" width="1200" height="396" viewBox="0 0 1200 396">
    <polygon points="534,396 760,290 1080,0 1200,0 1200,396" fill="var(--orange)"/>
    <polygon points="905,5 1080,105 1080,300 905,396 730,300 730,105" fill="#fff"/>
    <defs><linearGradient id="deskPhoto" x1="0" y1="0" x2="1" y2="1"><stop offset="0" stop-color="#eceef0"/><stop offset="1" stop-color="#9aa3ad"/></linearGradient></defs>
    <polygon role="img" aria-label="Photo of a woman at a desk with a large monitor in an open office" points="905,25 1062,115 1062,290 905,380 748,290 748,115" fill="url(#deskPhoto)"/>
  </svg>
  <div class="eyebrow">Discover The</div>
  <h2>BENEFITS OF OUTSOURCING</h2>
  <ul>
    <li><b>Shed overhead</b> and invest in core resources.</li>
    <li><b>Reduce risk</b> – Lower headcount, infrastructure, and technology costs.</li>
    <li><b>Scale up and down</b> as needed.</li>
    <li><b>Focus on your business</b>, not on labor-intensive processes.</li>
    <li><b>Build customer affinity</b> with professional service teams.</li>
    <li><b>Continuous improvement</b> via performance management.</li>
    <li><b>Access data</b> to make better business decisions.</li>
  </ul>
</section>

<section class="outs">
  <h2>OUTSOURCING</h2>
  <div class="sub">Flexible, versatile, end-to-end outsourcing options to help you get more of what your business needs.</div>

  <div class="card orange" style="left:93px">
    <div class="panel-wrap"><div class="panel"><ul>
      <li>Improve satisfaction, eliminate backlog, and streamline order processing and enrollment support.</li>
      <li>Dedicated teams that focus on your KPIs to deliver real value.</li>
      <li>Gain insight with 360-degree analytics.</li>
    </ul></div></div>
    <div class="notch"></div>
    <div class="num">01</div><div class="title">Customer Service<br>Contact Center</div>
  </div>
  <div class="card blue" style="left:352px">
    <div class="panel-wrap"><div class="panel"><ul>
      <li>Boost uptime for users and employees with Level 1, 2, and 3 support.</li>
      <li>Build your knowledge library with meaningful information.</li>
      <li>Create a tech-forward service center with advanced call center technologies.</li>
    </ul></div></div>
    <div class="notch"></div>
    <div class="num">02</div><div class="title">Tech Support<br>Service Center</div>
  </div>
  <div class="card orange" style="left:610px">
    <div class="panel-wrap"><div class="panel"><ul>
      <li>Streamline business and back office processes that hold your team back.</li>
      <li>Manage complex transactions with a consistent, process-oriented approach.</li>
      <li>Offload manual document processing and data validation tasks.</li>
    </ul></div></div>
    <div class="notch"></div>
    <div class="num">03</div><div class="title">Business Process<br>Outsourcing</div>
  </div>
  <div class="card blue" style="left:868px">
    <div class="panel-wrap"><div class="panel"><ul>
      <li>Build a new service center from the ground up with leading CRM and telephony technology.</li>
      <li>Benefit from omnichannel phone, email, chat, and SMS.</li>
      <li>Capture 360-degree business insights via custom reporting and analytics.</li>
    </ul></div></div>
    <div class="notch"></div>
    <div class="num">04</div><div class="title">End-to-End<br>Solutions</div>
  </div>
</section>

<section class="market">
  <h2>WE SERVE YOUR MARKET</h2>
  <div class="sub">We serve commercial businesses and federal and state government. We can serve you.</div>
  <div class="arrow left">‹</div><div class="arrow right">›</div>
  <div class="tile" style="left:93px"><div class="photo" role="img" aria-label="Photo of a team working on laptops in a lounge" style="background:linear-gradient(135deg,#6b5a4c,#2f2a28)"></div><div class="kind">Insurance</div><div class="name">Contact Center Services</div></div>
  <div class="tile" style="left:350px"><div class="photo" role="img" aria-label="Photo of two colleagues at a white meeting table" style="background:linear-gradient(135deg,#eeeeee,#a9a9a9)"></div><div class="kind">Government</div><div class="name">Contact Center Solution</div></div>
  <div class="tile" style="left:606px"><div class="photo" role="img" aria-label="Photo of smiling team members in an office" style="background:linear-gradient(135deg,#8a7462,#3d3530)"></div><div class="kind">Customer</div><div class="name">Service For Ecommerce</div></div>
  <div class="tile" style="left:862px"><div class="photo" role="img" aria-label="Photo of a busy open-plan operations floor" style="background:linear-gradient(135deg,#9a8f86,#4b4642)"></div><div class="kind">Business Process</div><div class="name">Outsourcing Solutions</div></div>
</section>

<section class="econ">
  <h2>THE ECONOMICS OF OUTSOURCING</h2>
  <p>Take a hard look at your operating model. What overhead and labor costs can you shed? How can you change in order to become more competitive? Our eBook shows you the way.</p>
  <div class="pill"></div>
  <div class="field" style="left:290px">Your Name:</div>
  <div class="field" style="left:500px">Your Email:</div>
  <div class="go">LINK TO EBOOK</div>
</section>

<footer class="footer">
  <div class="fcol" style="left:93px"><h3>Quick links</h3><ul><li>Home</li><li>Markets We Serve</li><li>About Us</li><li>Contact</li><li>Apply Today</li></ul></div>
  <div class="fcol" style="left:274px"><h3>Market We Serve</h3><ul><li>Government</li><li>Finance, Healthcare &amp; Insurance</li><li>Customer Service Contact Center</li><li>Tech Support Contact Center</li><li>Business Process Outsourcing</li><li>eCommerce</li><li>Analytics for Contact Centers</li></ul></div>
  <div class="fcol" style="left:531px"><h3>Contacts</h3><div class="addr">Harbor Point 18 Meridian Way Suite Four,<br>Unit 210 Eastport, ME 04000</div><div class="line">+1 555.014.2290</div><div class="line" style="margin-top:28px">info@korvanta.com</div></div>
  <div class="fcol" style="left:806px"><h3>Reach Us</h3></div>
  <div class="ffield" style="top:89px;width:264px;height:34px">Name:</div>
  <div class="ffield" style="top:134px;width:264px;height:32px">Email:</div>
  <div class="ffield" style="top:172px;width:298px;height:72px">Message:</div>
  <div class="send">SEND</div>
  <div class="socials"><span></span><span></span><span></span><span></span></div>
  <div class="copy">COPYRIGHT © 2020 <span>KORVANTA</span>. ALL RIGHTS RESERVED.</div>
</footer>

</body>
</html>
```